Alarm System package Ad for Chatterbox and flyer

Looking to create a Chatterbox add & flyer (A4) for an alarm system package
It will be used in paid Chatterbox advertising and letterbox drops
Once design is decided I will require 2-3 different pricing versions but using the same layout/design

The alarm package is a very cheap deal and the system itself if most suitable for smaller homes and smaller businesses.
The package includes back to base alarm monitoring on a contract for a minimum 12 months. This is at an additional cost (terms and conditions will explain this)

Target Market(s)

families, small business owners, home owners,

Industry/Entity Type

Advertising

Font styles to use
Sans Serif

Colors

Designer to choose colors to be used in the design.

Requirements
Must have
• Harbourline Alarms logo to be easily visible
• the alarm package will be priced at $299 (and 2 other version will be required upon approval of design)
• it will need a section to state terms and conditions apply
• KWL Linked (logo)
• Image of the parts
• minimal wording eg'Fully installed monitored alarm system" then the price
Nice to have
• family and/or home in the background
• Colors similar to my logo
• Logo on the ad
Should not have
• must not have a corporate feel

```html
<!DOCTYPE html>
<html lang="en">
<head>
<meta charset="utf-8">
<title>Harbourline Alarms – $299 Alarm Package Flyer</title>
<link href="https://fonts.googleapis.com/css2?family=Oswald:wght@500;700&family=Roboto:wght@400;500;700&display=swap" rel="stylesheet">
<style>
  :root {
    --navy: #1d3a7a;
    --navy-deep: #172f66;
    --sky: #0a9bd8;
    --sky-light: #3cb4e6;
    --ink: #2a2a2a;
    --paper: #ffffff;
    --backdrop: #e9ebee;
    --device: #dfe3e6;
  }
  * { box-sizing: border-box; margin: 0; padding: 0; }
  html, body { width: 1200px; height: 966px; overflow: hidden; }
  body { background: var(--backdrop); font-family: "Roboto", Arial, sans-serif; position: relative; }

  .flyer {
    position: absolute; left: 275px; top: 23px;
    width: 650px; height: 920px;
    background: var(--paper);
    overflow: hidden;
    box-shadow: 0 4px 18px rgba(0,0,0,.18);
  }
  .flyer__hero { position: absolute; left: 0; top: 0; width: 650px; height: 560px; display: block; }

  .flyer__intro {
    position: absolute; left: 40px; top: 566px; width: 240px;
    font-size: 13.5px; line-height: 1.3; color: var(--ink);
  }
  .flyer__tagline {
    position: absolute; left: 40px; top: 634px;
    font-family: "Oswald", Arial, sans-serif; font-weight: 500;
    font-size: 31px; line-height: 1.2; letter-spacing: .3px;
    color: var(--sky); text-transform: uppercase;
  }
  .flyer__price {
    position: absolute; left: 40px; top: 660px;
    font-family: "Oswald", Arial, sans-serif; font-weight: 700;
    color: var(--navy); line-height: 1;
    display: flex; align-items: flex-end;
  }
  .flyer__price-currency { font-size: 36px; margin-bottom: 34px; margin-right: 2px; }
  .flyer__price-amount { font-size: 160px; letter-spacing: -3px; }

  .flyer__parts {
    position: absolute; left: 350px; top: 568px; width: 270px; height: 192px;
    border-radius: 8px;
    background: linear-gradient(135deg, #f4f6f7 0%, var(--device) 60%, #c9ced2 100%);
  }
  .flyer__terms {
    position: absolute; left: 350px; top: 772px; width: 275px;
    font-size: 9.5px; line-height: 1.3; color: var(--ink);
  }

  .flyer__rule {
    position: absolute; left: 0; right: 0; top: 826px;
    height: 3px; background: var(--navy);
  }
  .flyer__footer {
    position: absolute; left: 0; right: 0; top: 829px; bottom: 0;
    display: flex; align-items: center; justify-content: center; gap: 38px;
  }
  .brand { display: flex; align-items: center; gap: 10px; color: var(--navy); font-weight: 700; }
  .brand__dot { width: 26px; height: 26px; border-radius: 50%; background: var(--sky); }
  .brand__square { width: 26px; height: 26px; background: var(--navy); }
  .brand__name { font-size: 26px; letter-spacing: .5px; }
  .brand--client .brand__name { text-transform: uppercase; font-size: 22px; letter-spacing: 1.5px; }
  .footer__divider { width: 2px; height: 44px; background: #c7ccd6; }
</style>
</head>
<body>
  <article class="flyer">
    <svg class="flyer__hero" viewBox="0 0 650 560">
      <defs>
        <linearGradient id="photoTone" x1="0" y1="0" x2="0" y2="1">
          <stop offset="0" stop-color="#6e5d4c"/>
          <stop offset=".55" stop-color="#5d6e48"/>
          <stop offset="1" stop-color="#4f8a2a"/>
        </linearGradient>
        <linearGradient id="navySweep" x1="0" y1="0" x2="1" y2="1">
          <stop offset="0" stop-color="#2a67b3"/>
          <stop offset="1" stop-color="#172f66"/>
        </linearGradient>
      </defs>
      <rect x="0" y="0" width="650" height="560" fill="#ffffff"/>
      <circle cx="440" cy="120" r="440" fill="url(#navySweep)"/>
      <circle cx="462" cy="110" r="418" fill="#ffffff"/>
      <circle cx="470" cy="108" r="408" fill="#0a9bd8"/>
      <circle cx="490" cy="100" r="392" fill="#ffffff"/>
      <circle cx="500" cy="96" r="382" fill="url(#photoTone)" role="img"
              aria-label="Photo: a smiling family playing on the front lawn of their home"/>
    </svg>

    <p class="flyer__intro">The alarm package is a very cheap deal and the system itself is most suitable for smaller homes and smaller businesses.</p>
    <h2 class="flyer__tagline">Secure your home</h2>
    <div class="flyer__price">
      <span class="flyer__price-currency">$</span>
      <span class="flyer__price-amount">299</span>
    </div>

    <div class="flyer__parts" role="img" aria-label="Product photo: alarm keypad, two motion sensors, door sensor and key remote"></div>
    <p class="flyer__terms">The package includes back to base alarm monitoring on a contract for a minimum 12 months. This is at an additional cost (terms and conditions will explain this)</p>

    <div class="flyer__rule"></div>
    <footer class="flyer__footer">
      <div class="brand brand--partner">
        <span class="brand__dot"></span>
        <span class="brand__name">KWL Linked</span>
      </div>
      <span class="footer__divider"></span>
      <div class="brand brand--client">
        <span class="brand__square"></span>
        <span class="brand__name">Harbourline Alarms</span>
      </div>
    </footer>
  </article>
</body>
</html>
```